Webdesign für einen Softwarehersteller
Zielgruppe
Wir sind Softwarehersteller einer Arbeitsschutz Management Software. Unser Leistungsumfang beträgt
a) die Analyse, Beurteilung und Risikoeinschätzung von Gefährdungen an einem Arbeitsplatz, einer Maschine oder Tätigkeit
b) die Unterweisung von Mitarbeitern
c) ein Risiko- und Maßnahmenmanagement
d) ein Unfallmanagement bei welchem Unfälle erfasst, ausgewertet und präventive Maßnahmen ergriffen werden
e) ein Management zur Verwaltung von Gefahrstoffen inkl. der Ableitung von präventiven Maßnahmen
f) ein Tool zur Auditierung von Prozessen, wie z.B. ISO-Normen
Unsere Zielgruppe sind Industrieunternehmen ab 500 Mitarbeitern. Der Traumkunde hat 4000 - 8000 Mitarbeiter. Unsere Software ist multilingual und kann auch weltweit eingesetzt werden womit auch weltweit operierende Konzerne zu unserer Zielgruppe gehören.
Mit unserer Software dokumentiert das Unternehmen alle notwendigen Prozesse zur Einhaltung des Arbeitsschutzes. Die Software unterstützt dabei das Unternehmen, die Menschen im Unternehmen best möglich zu schützen und allen rechtlichen Anforderungen gerecht zu werden.
Aufgabenstellung
Hallo Designer:innen,
zuerst möchte ich mich bei euch bedanken, dass Ihr euch an unserem Projekt beteiligt. Wir suchen eine Homepage, sehr clean, sehr modern und passend zu einem Softwareprodukt z.B. https://brennlaub.com/seiten-vorlagen (Kalvorix Theme). Wir legen Wert auf Struktur, Übersichtlichkeit, Modern.
Textinhalte findet Ihr auf der bestehenden Homepage.
WICHTIG!!!
a) Die bestehende Homepage dient als Inhaltsvorlage. Wir finden die Homepage nicht gut!
b) Wir erwarten, ein Hochwertiges Design sowie eine durchdachte Aufteilung der Homepage. Wenn Ihr z.B. der Meinung seid, dass auf der Landingpage eine Produktgallerie mit Bildern notwendig ist, dann fügt diese bitte ein und verwendet Demo-Bilder. Wir liefern gerne später Inhalte für die Bereiche. Die neue Webseite darf gerne von der bestehenden Struktur abweichen.
c) Selvadon wird ein neues, moderneres Logo erhalten. Das neue Logo findet Ihr unter
https://stage.selvadon.de/wp-content/uploads/2022/02/test_logo1.png
https://stage478.selvadon.de/wp-content/uploads/2022/03/Logo_web.png

```html
<!DOCTYPE html>
<html lang="de">
<head>
<meta charset="utf-8">
<title>Selvadon – Webdesign Arbeitsschutzsoftware</title>
<link rel="stylesheet" href="https://fonts.googleapis.com/css2?family=Montserrat:wght@300;400;500;600&family=EB+Garamond:ital,wght@0,400;1,400&display=swap">
<style>
:root{
  --board:#7d7d7d;
  --white:#ffffff;
  --ink:#333a36;
  --muted:#6c726e;
  --green:#7cc242;
  --green-dark:#2e4a24;
  --footer:#4f9a10;
  --cyan:#33b4d2;
  --cyan-light:#a9e5f2;
  --hero-a:#1fa6df;
  --hero-b:#7ee0f4;
  --line:#d9dedb;
}
*{box-sizing:border-box;margin:0;padding:0}
html,body{width:1186px;height:1200px;overflow:hidden;background:var(--board)}
body{font-family:"Montserrat",sans-serif;color:var(--ink)}
.board{position:absolute;left:0;top:0;width:1910px;height:1932px;transform:scale(0.62094);transform-origin:0 0;background:var(--board)}
.page{position:absolute;background:var(--white);overflow:hidden}
.p-home{left:128px;top:90px;width:394px;height:1597px}
.p-modules{left:560px;top:90px;width:391px;height:1750px}
.p-company{left:988px;top:88px;width:389px;height:1554px}
.p-contact{left:1411px;top:88px;width:390px;height:973px}

.nav{height:18px;display:flex;justify-content:center;align-items:center;gap:18px;font-size:4.6px;letter-spacing:.3px;color:var(--ink)}
.nav .active{color:var(--green)}
.hero{height:118px;position:relative;background:linear-gradient(100deg,#3b8fd8 0%,var(--hero-a) 30%,var(--hero-b) 55%,var(--hero-a) 80%,#1f7fd0 100%)}
.hero-mark{position:absolute;left:50%;top:22px;transform:translateX(-50%);width:100px;height:72px;background:rgba(255,255,255,.55);display:flex;flex-direction:column;align-items:center;justify-content:flex-end;padding-bottom:10px;gap:16px}
.hero-mark .sq{width:22px;height:22px;background:var(--green)}
.wordmark{font-weight:400;letter-spacing:3px;font-size:9px;color:#2c3a33}

.title{text-align:center;font-weight:300;letter-spacing:3.2px;font-size:11px;color:#2c3a33;line-height:1.9}
.title.green{color:var(--green)}
.label{font-size:3.8px;letter-spacing:.8px;color:var(--green);font-weight:500;margin-bottom:5px;text-transform:uppercase}
.txt{font-size:4.6px;line-height:1.75;color:var(--muted)}
.txt p+p{margin-top:5px}
.btns{display:flex;justify-content:center;gap:4px}
.btn{height:12px;border-radius:7px;padding:0 12px;display:flex;align-items:center;font-size:3.6px;letter-spacing:.6px;text-transform:uppercase}
.btn.dark{background:var(--green-dark);color:#fff}
.btn.line{border:.8px solid #b5bcb8;color:var(--muted)}
.btn.green{background:var(--green);color:#fff}
.btn.big{height:19px;border-radius:10px;padding:0 15px;font-size:4.4px}

.chev{list-style:none;font-size:4.8px;color:var(--ink);line-height:1}
.chev li{display:flex;gap:6px;margin-bottom:11px}
.chev li::before{content:"»";color:var(--green);font-size:7px;line-height:.7}

.img{display:block}
.portrait{width:60px;height:60px;margin:0 auto;background:linear-gradient(180deg,#eef1f2,#c9d0d3)}
.caption{text-align:center;font-size:3px;color:var(--muted);margin-top:4px;line-height:1.4}
.ask{font-family:"EB Garamond",serif;font-size:10px;text-align:center;color:#2c3a33;margin-top:30px}
.ask-txt{text-align:center;font-size:4.6px;line-height:1.8;color:var(--muted);margin:16px auto 12px;width:200px}
.partners{display:flex;justify-content:space-between;align-items:center;padding:0 55px;margin-top:50px}
.partners span{font-size:10px;font-weight:600;color:#3b4a55;letter-spacing:.3px}

.footer{position:absolute;left:0;right:0;bottom:0;background:var(--footer);padding:38px 33px 0;display:grid;grid-template-columns:1fr 1fr 1fr;gap:10px}
.footer h6{font-size:3px;font-weight:400;letter-spacing:.6px;color:rgba(255,255,255,.6);margin-bottom:18px}
.footer li{list-style:none;font-size:3.6px;color:#e8f5dc;line-height:2.7}
.footer .fmark{position:absolute;left:50%;bottom:18px;transform:translateX(-50%);font-size:8px;letter-spacing:3px;color:rgba(255,255,255,.28)}
.badge{width:22px;height:12px;border-radius:6px;background:#a6e07a;margin-top:6px}

.band-app{background:var(--cyan-light);height:177px;position:relative;margin-top:28px}
.app{position:absolute;left:63px;top:8px;width:276px;height:160px;background:#fff;box-shadow:0 0 3px rgba(0,0,0,.1)}
.app-bar{height:15px;background:#3f9a2a;color:#fff;font-size:4px;display:flex;align-items:center;padding-left:18px}
.app-side{position:absolute;left:0;top:15px;bottom:0;width:74px;background:#e4f3d6}
.app-rows{position:absolute;left:80px;top:62px;right:12px}
.app-rows div{height:9px;border-bottom:.5px solid var(--line)}
.app-rows .sel{background:#cfd4d1}
.arrow{position:absolute;top:80px;color:#fff;font-size:10px}
</style>
</head>
<body>
<div class="board">

<!-- HOME -->
<section class="page p-home">
  <nav class="nav"><span class="active">HOME</span><span>SOFTWAREMODULE</span><span>UNTERNEHMEN</span><span>KONTAKT</span></nav>
  <div class="hero" role="img" aria-label="Labormotiv mit Mikroskop, DNA-Strang und Tastatur in Blautönen"><div class="hero-mark"><span class="sq"></span><span class="wordmark">SELVADON</span></div></div>
  <h2 class="title" style="margin-top:18px">ARBEITSSCHUTZSOFTWARE</h2>
  <div style="display:grid;grid-template-columns:1fr 1fr;gap:16px 16px;padding:12px 84px 0 94px">
    <div><div class="label">Vielseitige Entlastung</div><div class="txt">Die Selvadon Arbeitsschutz Software entlastet alle Beteiligten im Arbeitsschutz, angefangen bei den Vorgesetzten und Fachkräften für Arbeitssicherheit, über die Mitarbeiter mit Kontrollfunktionen bis hin zu den IT Administratoren.</div></div>
    <div><div class="label">Mehr Effizienz und Schutz</div><div class="txt">Selvadon besitzt eine Vielzahl an automatisierten Abläufen und Schutzfunktionen. Dadurch werden Mitarbeiter wie auch Verantwortliche optimal geschützt.</div></div>
    <div><div class="label">Perfekte Oberflächen</div><div class="txt">Selvadon bietet eine intuitive, selbsterklärende und sehr einfach zu bedienende Oberfläche. Dies führt zu einer sehr hohen Akzeptanz und minimalem Schulungsaufwand.</div></div>
    <div><div class="label">Transparente Prozesse</div><div class="txt">Durch das Zusammenwirken aller Module werden Unstimmigkeiten im Arbeitsschutz automatisiert erkannt und per Dashboard dem jeweiligen Verantwortlichen gemeldet.</div></div>
  </div>
  <div class="btns" style="margin-top:22px"><span class="btn dark">Funktionen</span><span class="btn line">Warum Selvadon</span></div>
  <div class="band-app">
    <span class="arrow" style="left:44px">‹</span><span class="arrow" style="right:38px">›</span>
    <div class="app">
      <div class="app-bar">Vorfall hinzufügen oder editieren</div>
      <div class="app-side"></div>
      <div class="app-rows"><div></div><div></div><div></div><div></div><div></div><div class="sel"></div><div></div><div></div><div></div><div></div><div></div></div>
    </div>
  </div>
  <h2 class="title" style="margin-top:26px">ARBEITSSCHUTZ FUNKTIONEN &amp; MODULE</h2>
  <p class="txt" style="padding:8px 68px 0">Unsere Software für Arbeitsschutz bietet eine breite Palette an Modulen und Funktionen, um Sie im Bereich Arbeitsschutz und Management bestmöglich zu unterstützen:</p>
  <div style="display:grid;grid-template-columns:1fr 1fr;padding:12px 72px 0">
    <ul class="chev"><li>Basisfunktionen</li><li>Gefährdungsbeurteilung</li><li>Unterweisung</li><li>Unfallmanagement</li><li>Gefahrstoffmanagement</li><li>Vorsorgeuntersuchungen</li><li>Qualifikationsmatrix</li></ul>
    <ul class="chev"><li>Maßnahmenmanagement</li><li>Auditierung</li><li>Compliance</li><li>Dateiarchiv</li><li>Controlling und Management</li><li>Multilingual verfügbar</li></ul>
  </div>
  <div class="btns" style="margin-top:10px"><span class="btn dark">Funktionen im Detail</span><span class="btn green">Präsentationstermin vereinbaren</span></div>
  <div class="img" role="img" aria-label="Laborantin mit Schutzbrille und Reagenzglas vor einem Virusmodell" style="height:144px;margin-top:36px;background:linear-gradient(90deg,#e9f4f8 0%,#bfe4ef 40%,#4fb1cf 70%,#2a86b8 100%)"></div>
  <h2 class="title" style="margin-top:22px">WO FÜR STEHT SELVADON?</h2>
  <div class="txt" style="padding:12px 46px 0"><p>Als „Praetorium“ wurde in einem römischen Legionslager das Zelt des Befehlshabers bezeichnet – der sicherste Platz im Lager. Prätorianer gehörten der kaiserlichen Gardetruppe an, die das Prätorium beschützt haben. Arbeitsschützer sind die heutigen Prätorianer, die das Unternehmen vor Gefahren und Unfällen beschützen.</p><p>Selvadon wird gemeinsam mit unserem Kompetenzteam entwickelt. Zum Kompetenzteam gehören viele Fachkräfte für Arbeitssicherheit die in den Unternehmen direkt an der Basis arbeiten – bis hin zu hochqualifizierten Beratern und Autoren. Diese Mischung macht unsere Software so perfekt, da Sie exakt die Wünsche, Bedürfnisse und Funktionen abbildet, die jeden Tag in den Unternehmen benötigt werden.</p></div>
  <div class="btns" style="margin-top:22px"><span class="btn dark">Arbeitsschutz Software</span><span class="btn line">Unternehmen</span></div>
  <div class="portrait" role="img" aria-label="Porträt eines Ansprechpartners" style="margin-top:40px"></div>
  <div class="caption">Tobias Rennert<br>Ihr persönlicher Ansprechpartner</div>
  <div class="ask">An Selvadon interessiert?</div>
  <div class="ask-txt">Nehmen Sie jetzt Kontakt auf und vereinbaren Sie Ihren unverbindlichen Beratungs- und Präsentationstermin.</div>
  <div class="btns"><span class="btn green big">Präsentationstermin vereinbaren</span></div>
  <div class="partners" style="padding:0 30px;margin-top:44px"><span>KALDREM</span><span>VOSTA</span><span>BRANDELL</span><span>TEVRIN</span></div>
  <footer class="footer" style="height:158px">
    <div><h6>ARBEITSSCHUTZ SOFTWARE MODULE</h6><ul><li>Basisfunktionen</li><li>Gefährdungsbeurteilung</li><li>Unterweisung</li><li>Unfallmanagement</li><li>Gefahrstoffmanagement</li><li>Auditierung</li><li>Compliance</li></ul></div>
    <div><h6>INFORMATIONEN</h6><ul><li>Unternehmen</li><li>Präsentationstermin</li><li>Kontakt</li></ul></div>
    <div><h6>RECHTLICHES</h6><ul><li>AGB</li><li>Datenschutz</li><li>Cookies</li><li>Impressum</li></ul><h6 style="margin:10px 0 0">PARTNER</h6><div class="badge"></div></div>
    <span class="fmark">SELVADON</span>
  </footer>
</section>

<!-- SOFTWAREMODULE -->
<section class="page p-modules">
  <nav class="nav"><span>HOME</span><span class="active">SOFTWAREMODULE</span><span>UNTERNEHMEN</span><span>KONTAKT</span></nav>
  <div class="hero" role="img" aria-label="Wissenschaftlerin mit Reagenzglas, Laborgläser und DNA-Strang in Blautönen"><div class="hero-mark"><span class="sq"></span><span class="wordmark">SELVADON</span></div></div>
  <h2 class="title" style="margin-top:14px">ARBEITSSCHUTZ<br>SOFTWAREMODULE</h2>
  <h2 class="title green" style="margin-top:2px">BASISFUNKTION</h2>
  <p class="txt" style="padding:10px 86px 0">Mit dem Basismodul werden alle Grundfunktionen, welche für den Betrieb von Selvadon notwendig sind, bereitgestellt. Neben den Grundfunktionen beinhaltet das Basismodul wichtige Features, die für alle weiteren Module systemübergreifend genutzt werden können.</p>
  <div class="txt" style="display:grid;grid-template-columns:1fr 1fr;gap:14px;padding:12px 84px 0 90px;font-size:4.3px">
    <div><p>Dokumentationsplattform für Vorgesetzte, Ermittler, Unfallerfasser und Gefahrstoffbeauftragte</p><p>Managementplattform für Fachkräfte der Arbeitssicherheit und Auditoren</p><p>Controlling-Plattform für Vorgesetzte mit Kontrollfunktionalitäten, Manager, Geschäftsführer und Betriebsräte</p><p>Umfangreiche Organisations- und Mitarbeiterverwaltung sowie die Verwaltung der Berechtigungsstrukturen innerhalb der Software</p><p>Dateiarchiv zur Ablage und Verwaltung von Dokumenten rund um den Bereich des Arbeitsschutzes</p><p>Grundfunktionen für das Maßnahmenmanagement über welches die Inhalte und Aufgaben aus den einzelnen Modulen verwaltet werden</p></div>
    <div><p>Vorsorgemanagement über welches Vorsorgeuntersuchungen im Unternehmen konfiguriert und verwaltet werden</p><p>Qualifikationsmanagement über welches Qualifikationen im Unternehmen konfiguriert und verwaltet werden</p><p>Erstellen und Verwalten von Betriebsanweisungen inkl. eines Formulargenerators</p><p>Recherchesystem über welches die Fachkräfte für Arbeitssicherheit Informationen aus den einzelnen Standorten oder Abteilungen abrufen können</p><p>Multilinguale Bereitstellung der Software zur Nutzung von Selvadon in verschiedenen Landessprachen</p></div>
  </div>
  <div class="btns" style="margin-top:16px"><span class="btn line">Mehr zu den Basisfunktionen</span><span class="btn green">Termin vereinbaren</span></div>

  <h2 class="title green" style="margin-top:28px">GEFÄHRDUNGSBEURTEILUNG</h2>
  <div class="txt" style="padding:14px 60px 0 98px"><p>Mit Selvadon erstellen Sie schnell, einfach und komfortabel in wenigen Schritten eine Gefährdungsbeurteilung. Die klare und selbsterklärende Benutzeroberfläche führt zu einer sehr hohen Akzeptanz unter Ihren Mitarbeitern und reduziert gleichzeitig den Schulungsaufwand auf ein Minimum.</p><p>Das Modul der Gefährdungsbeurteilung ist gekoppelt mit weiteren Modulen wie z.B. dem Vorsorge- und Qualifikationssystem sowie dem Unterweisungsmanagement. Maßnahmen aus einer Gefährdungsbeurteilung werden an das zentrale Maßnahmenmanagement übergeben, in welchem auch Maßnahmen aus anderen Modulen geführt und bearbeitet werden.</p></div>
  <div class="btns" style="margin-top:14px"><span class="btn line">Mehr zur Gefährdungsbeurteilung</span><span class="btn green">Termin vereinbaren</span></div>

  <h2 class="title green" style="margin-top:24px">UNTERWEISUNG</h2>
  <div class="txt" style="padding:14px 60px 0 100px"><p>Arbeiten und erstellen Sie schnell, einfach und komfortabel in wenigen Schritten eine Unterweisung für Ihre Mitarbeiter. Die klare und geführte Benutzeroberfläche hilft Ihnen bei der Erstellung Ihrer eigenen Unterweisungen.</p><p>Das Modul bietet Ihren Vorgesetzten mehrere Varianten der Unterweisung. So können mit Selvadon klassische Sammelunterweisungen, Erstunterweisungen sowie Onlineunterweisungen durchgeführt werden.</p></div>
  <div class="btns" style="margin-top:14px"><span class="btn line">Unterweisung im Detail</span><span class="btn green">Termin vereinbaren</span></div>

  <h2 class="title green" style="margin-top:28px">UNFALLMANAGEMENT</h2>
  <div class="txt" style="padding:14px 60px 0 100px"><p>Mit Selvadon führen Sie ganz einfach Ihr digitales Unfallsystem und profitieren bereits nach kurzer Zeit aus einer Vielzahl an Statistiken über das gesamte Unternehmen.</p><p>Zum Unfallmanagement zählt das Erfassen von Unfällen (Beinaheunfälle), Verbandbucheinträgen und Unfallmeldungen.</p><p>Basierend auf den erhobenen Daten lassen sich tagesaktuelle Statistiken über Unfallquoten, Verletzungsarten, Ausfalltage, Ausfallzeiten, 1000-Mann-Quoten usw. erstellen.</p></div>
  <div class="btns" style="margin-top:14px"><span class="btn line">Unfallmanagement im Detail</span><span class="btn green">Termin vereinbaren</span></div>

  <h2 class="title green" style="margin-top:26px">GEFAHRENSTOFFMANAGEMENT</h2>
  <div class="txt" style="padding:14px 64px 0 100px"><p>Selvadon unterstützt Sie sowohl bei der Verwaltung Ihrer Gefahrstoffe im Unternehmen als auch bei den Freigabeprozessen, Dokumentenablagen, Statistiken, Verwendungsnachweisen usw.</p><p>Profitieren Sie bei Selvadon von der automatisierten Kopplung zwischen den einzelnen Modulen. So werden z.B. Gefahrstoffe direkt mit einer Gefährdungsbeurteilung verknüpft.</p><p>Zu jedem Gefahrstoff lassen sich umfangreiche Daten hinterlegen und Sie erhalten Zugriff auf über 60000 Inhaltsstoffe mit bis zu 200 Einzelangaben je Gefahrstoff.</p><p>Zudem erfolgt eine automatische Substitutionsprüfung sowie eine Prüfungen auf REACH-Verbote.</p></div>
  <div class="btns" style="margin-top:14px"><span class="btn line">Gefahrstoffmanagement im Detail</span><span class="btn green">Termin vereinbaren</span></div>

  <h2 class="title green" style="margin-top:26px">COMPLIANCE <span style="letter-spacing:.5px;font-size:9px">ab Q4 / 2021</span></h2>
  <div class="txt" style="padding:14px 64px 0 102px"><p>Das Compliance – Modul verbindet ein Rechtskataster mit den bestehenden Selvadon-Prozessen. So können Gesetzesänderungen über das Compliance – Modul bewertet und dokumentiert werden.</p><p>Notwendige Änderungen oder Umsetzungen werden über das integrierte Maßnahmenmanagement dokumentiert und mit den betreffenden Abteilungen kommuniziert.</p></div>
  <div class="btns" style="margin-top:16px"><span class="btn line">Details zum Compliance Modul</span><span class="btn green">Termin vereinbaren</span></div>

  <div class="portrait" role="img" aria-label="Porträt eines Ansprechpartners" style="margin-top:52px"></div>
  <div class="caption">Tobias Rennert<br>Ihr persönlicher Ansprechpartner</div>
  <div class="ask">An Selvadon interessiert?</div>
  <div class="ask-txt">Nehmen Sie jetzt Kontakt auf und vereinbaren Sie Ihren unverbindlichen Beratungs- und Präsentationstermin.</div>
  <div class="btns"><span class="btn green big">Präsentationstermin vereinbaren</span></div>
  <div class="partners" style="padding:0 30px;margin-top:46px"><span>KALDREM</span><span>VOSTA</span><span>BRANDELL</span><span>TEVRIN</span></div>
  <footer class="footer" style="height:158px">
    <div><h6>ARBEITSSCHUTZ SOFTWARE MODULE</h6><ul><li>Basisfunktionen</li><li>Gefährdungsbeurteilung</li><li>Unterweisung</li><li>Unfallmanagement</li><li>Gefahrstoffmanagement</li><li>Auditierung</li><li>Compliance</li></ul></div>
    <div><h6>INFORMATIONEN</h6><ul><li>Unternehmen</li><li>Präsentationstermin</li><li>Kontakt</li></ul></div>
    <div><h6>RECHTLICHES</h6><ul><li>AGB</li><li>Datenschutz</li><li>Cookies</li><li>Impressum</li></ul><h6 style="margin:10px 0 0">PARTNER</h6><div class="badge"></div></div>
    <span class="fmark">SELVADON</span>
  </footer>
</section>

<!-- UNTERNEHMEN -->
<section class="page p-company">
  <nav class="nav"><span>HOME</span><span>SOFTWAREMODULE</span><span class="active">UNTERNEHMEN</span><span>KONTAKT</span></nav>
  <div class="hero" role="img" aria-label="Digitale Diagramme und Datenoberflächen in Blautönen"><div class="hero-mark"><span class="sq"></span><span class="wordmark">SELVADON</span></div></div>
  <h2 class="title" style="margin-top:14px">ARBEITSSCHUTZ</h2>
  <h2 class="title green">UNTERNEHEMENSKOZEPT</h2>
  <ul class="chev" style="padding:24px 40px 0 82px;font-size:5.6px;line-height:1.6">
    <li style="margin-bottom:8px">Analyse, Beurteilung und Risikoeinschätzung von Gefährdungen an einem Arbeitsplatz, einer Maschine oder Tätigkeit</li>
    <li style="margin-bottom:8px">Unterweisung von Mitarbeitern</li>
    <li style="margin-bottom:8px">Risiko- und Maßnahmenmanagement</li>
    <li style="margin-bottom:8px">Unfallmanagement bei welchem Unfälle erfasst, ausgewertet und präventive Maßnahmen ergriffen werden</li>
    <li style="margin-bottom:8px">Management zur Verwaltung von Gefahrstoffen inklusive der Ableitung von präventiven Maßnahmen</li>
    <li style="margin-bottom:8px">Tool zur Auditierung von Prozessen, wie z.B. ISO-Normen</li>
  </ul>
  <p style="font-family:'EB Garamond',serif;font-style:italic;font-size:8.8px;line-height:1.55;color:#2c3a33;padding:28px 34px 0">Menschlichkeit, langjährige Partnerschaften und Arbeiten auf Augenhöhe stehen bei uns im Fokus. Wir lieben unsere Arbeit, sind für unsere Mitarbeiter da und bewegen Berge für unsere Kunden.</p>
  <h2 class="title green" style="margin-top:26px">WER WIR SIND</h2>
  <p class="txt" style="padding:12px 30px 0;font-size:5.2px;text-align:center">Selvadon ist Teil der Norvek Docs GmbH – ein seit über 25 Jahren inhabergeführtes Familienunternehmen mit Traditionen, Werten und einem ganz tollen Team. Neben dem Bereich Arbeitsschutz haben wir auch Standbeine in Lumina Medical IT Services sowie als klassisches Systemhaus.</p>
  <div class="img" role="img" aria-label="Teamfoto mit drei Mitarbeitern in weißen Hemden vor grauer Wand" style="height:117px;margin-top:24px;background:linear-gradient(90deg,#bfc3c4 0%,#dcdfe0 45%,#c7cbcc 100%)"></div>
  <div style="display:grid;grid-template-columns:1fr 1fr 1fr;text-align:center;font-family:'EB Garamond',serif;padding:6px 30px 0;font-size:5px;color:#2c3a33;line-height:1.9">
    <div>Jonas Wehrle<br><i style="color:var(--muted)">Head of Development</i></div>
    <div>Tobias Rennert<br><i style="color:var(--muted)">Head of Sales Department</i></div>
    <div>Stefan Albrecht<br><i style="color:var(--muted)">CEO &amp; Founder</i></div>
  </div>
  <p style="text-align:center;font-size:7px;line-height:2;color:var(--muted);padding:18px 42px 0">Selvadon wird gemeinsam mit unserem Kompetenzteam entwickelt. Zum Kompetenzteam gehören viele Fachkräfte für Arbeitssicherheit die in den Unternehmen direkt an der Basis arbeiten bis hin zu hochqualifizierten Beratern und Autoren. Diese Mischung macht unsere Software so perfekt da Sie exakt die Wünsche, Bedürfnisse und Funktionen abbildet, die jeden Tag in den Unternehmen benötigt werden.</p>
  <div style="background:var(--cyan);height:268px;margin-top:34px;padding:22px 10px 0;color:#fff">
    <h2 class="title" style="color:#fff;font-size:10px">DIE SELVADON FIRMENKULTUR</h2>
    <div style="display:grid;grid-template-columns:1fr 1fr;gap:18px 22px;margin-top:18px;font-size:3.4px;line-height:1.6">
      <div><svg width="12" height="12" viewBox="0 0 12 12"><rect x="2" y="5" width="8" height="6" fill="none" stroke="#fff" stroke-width="1"/><path d="M4 5V3h4v2" fill="none" stroke="#fff"/></svg><div style="font-family:'EB Garamond',serif;font-size:6px;margin:3px 0">Fort- und Weiterbildung</div>Wir fördern die Weiterbildung unserer Mitarbeiter mit regelmäßigen Schulungen, Seminaren und Kursen.</div>
      <div><svg width="12" height="12" viewBox="0 0 12 12"><path d="M6 10.5 1.5 6A2.5 2.5 0 0 1 6 3a2.5 2.5 0 0 1 4.5 3z" fill="none" stroke="#fff"/></svg><div style="font-family:'EB Garamond',serif;font-size:6px;margin:3px 0">Soulfood inklusive</div>Frisches Obst · Getränke · Kaffee &amp; Tee · gemeinsames Frühstück</div>
      <div><svg width="12" height="12" viewBox="0 0 12 12"><ellipse cx="6" cy="5.5" rx="5" ry="4" fill="none" stroke="#fff"/></svg><div style="font-family:'EB Garamond',serif;font-size:6px;margin:3px 0">Experten-Austausch</div>Unser Team arbeitet eng mit Beratern und Fachkräften zusammen und teilt Wissen in regelmäßigen Runden.</div>
      <div><svg width="12" height="12" viewBox="0 0 12 12"><path d="M2 2l8 8M10 2l-8 8" stroke="#fff"/></svg><div style="font-family:'EB Garamond',serif;font-size:6px;margin:3px 0">Kulinarisches</div>Gemeinsame Mittagessen und kleine Teamevents sorgen für gute Stimmung im gesamten Haus.</div>
      <div><svg width="12" height="12" viewBox="0 0 12 12"><path d="M2 10 10 2M6 2h4v4" fill="none" stroke="#fff"/></svg><div style="font-family:'EB Garamond',serif;font-size:6px;margin:3px 0">Flexibilität</div>Flexible Arbeitszeiten und mobiles Arbeiten ermöglichen eine gute Balance zwischen Beruf und Familie.</div>
      <div><svg width="12" height="12" viewBox="0 0 12 12"><circle cx="6" cy="6" r="4.5" fill="none" stroke="#fff"/></svg><div style="font-family:'EB Garamond',serif;font-size:6px;margin:3px 0">Spaß &amp; Action</div>Ausflüge, Sportevents und Feiern stärken den Zusammenhalt und bringen Abwechslung in den Alltag.</div>
    </div>
  </div>
  <div class="portrait" role="img" aria-label="Porträt eines Ansprechpartners" style="margin-top:32px"></div>
  <div class="caption">Tobias Rennert<br>Ihr persönlicher Ansprechpartner</div>
  <div class="ask">An Selvadon interessiert?</div>
  <div class="ask-txt">Nehmen Sie jetzt Kontakt auf und vereinbaren Sie Ihren unverbindlichen Beratungs- und Präsentationstermin.</div>
  <div class="btns"><span class="btn green big">Präsentationstermin vereinbaren</span></div>
  <div class="partners" style="padding:0 30px;margin-top:44px"><span>KALDREM</span><span>VOSTA</span><span>BRANDELL</span><span>TEVRIN</span></div>
  <footer class="footer" style="height:158px">
    <div><h6>ARBEITSSCHUTZ SOFTWARE MODULE</h6><ul><li>Basisfunktionen</li><li>Gefährdungsbeurteilung</li><li>Unterweisung</li><li>Unfallmanagement</li><li>Gefahrstoffmanagement</li><li>Auditierung</li><li>Compliance</li></ul></div>
    <div><h6>INFORMATIONEN</h6><ul><li>Unternehmen</li><li>Präsentationstermin</li><li>Kontakt</li></ul></div>
    <div><h6>RECHTLICHES</h6><ul><li>AGB</li><li>Datenschutz</li><li>Cookies</li><li>Impressum</li></ul><h6 style="margin:10px 0 0">PARTNER</h6><div class="badge"></div></div>
    <span class="fmark">SELVADON</span>
  </footer>
</section>

<!-- KONTAKT -->
<section class="page p-contact">
  <nav class="nav"><span>HOME</span><span>SOFTWAREMODULE</span><span>UNTERNEHMEN</span><span class="active">KONTAKT</span></nav>
  <div class="hero" style="height:116px" role="img" aria-label="Labormotiv mit Mikroskop und Laborgläsern in Blautönen"><div class="hero-mark"><span class="sq"></span><span class="wordmark">SELVADON</span></div></div>
  <div class="img" role="img" aria-label="Stadtplan mit Standortmarkierung" style="position:absolute;left:14px;top:162px;width:191px;height:190px;background:linear-gradient(120deg,#ecebe6 0%,#e3e1da 55%,#cfe6b8 100%)"></div>
  <div style="position:absolute;left:232px;top:245px;font-size:13px;letter-spacing:4px;color:#2c3a33">SELVADON</div>
  <div style="position:absolute;left:236px;top:277px;width:140px;display:grid;grid-template-columns:1fr 1fr;gap:14px 6px;font-size:3.4px;line-height:1.6;color:var(--muted)">
    <div><span style="font-size:2.8px;letter-spacing:.4px">ADRESSE</span><br>Lindenweg 12<br>72300 Talbach<br>Deutschland</div>
    <div><span style="font-size:2.8px;letter-spacing:.4px">E-MAIL</span><br>info@selvadon.de</div>
    <div><span style="font-size:2.8px;letter-spacing:.4px">TELEFON</span><br>+49 (0) 7000 - 123 4500</div>
    <div><span style="font-size:2.8px;letter-spacing:.4px">TELEFAX</span><br>+49 (0) 7000 12 34 56 78</div>
  </div>
  <div style="position:absolute;left:0;right:0;top:380px">
    <div style="text-align:center;font-size:3px;letter-spacing:.6px;color:var(--muted)">KONTAKTFORMULAR</div>
    <h2 class="title green" style="font-size:10px;margin-top:4px">SIE HABEN FRAGEN UND WÜNSCHE</h2>
    <div style="text-align:center;font-size:4px;color:var(--muted);margin-top:2px">Das Selvadon-Team steht Ihnen gerne zur Verfügung</div>
    <div style="padding:10px 26px 0;font-size:3.4px;color:var(--ink);display:grid;grid-template-columns:1fr 1fr;gap:4px 14px">
      <div style="grid-column:1/3">Name *</div>
      <div><div style="height:9px;border:.6px solid var(--line)"></div><span style="font-size:2.8px;color:var(--muted)">Vorname</span></div>
      <div><div style="height:9px;border:.6px solid var(--line)"></div><span style="font-size:2.8px;color:var(--muted)">Nachname</span></div>
      <div>E-Mail *<div style="height:9px;border:.6px solid var(--line);margin-top:2px"></div></div>
      <div>Telefon<div style="height:9px;border:.6px solid var(--line);margin-top:2px"></div></div>
      <div style="grid-column:1/3">Kommentar oder Nachricht *<div style="height:34px;border:.6px solid var(--line);margin-top:2px"></div></div>
      <div style="grid-column:1/3;font-size:3px;color:var(--muted)">☐ Ich habe die Datenschutzbestimmungen gelesen und akzeptiert.</div>
      <div><span class="btn green" style="height:9px;width:34px;padding:0 6px;font-size:2.8px">Absenden</span></div>
    </div>
  </div>
  <div style="position:absolute;left:0;right:0;top:562px">
    <div class="portrait" role="img" aria-label="Porträt eines Ansprechpartners"></div>
    <div class="caption">Tobias Rennert<br>Ihr persönlicher Ansprechpartner</div>
    <div class="ask" style="margin-top:18px">An Selvadon interessiert?</div>
    <div class="ask-txt">Nehmen Sie jetzt Kontakt auf und vereinbaren Sie Ihren unverbindlichen Beratungs- und Präsentationstermin.</div>
    <div class="btns"><span class="btn green big">Präsentationstermin vereinbaren</span></div>
    <div class="partners" style="padding:0 30px;margin-top:30px"><span>KALDREM</span><span>VOSTA</span><span>BRANDELL</span><span>TEVRIN</span></div>
  </div>
  <footer class="footer" style="height:158px">
    <div><h6>ARBEITSSCHUTZ SOFTWARE MODULE</h6><ul><li>Basisfunktionen</li><li>Gefährdungsbeurteilung</li><li>Unterweisung</li><li>Unfallmanagement</li><li>Gefahrstoffmanagement</li><li>Auditierung</li><li>Compliance</li></ul></div>
    <div><h6>INFORMATIONEN</h6><ul><li>Unternehmen</li><li>Präsentationstermin</li><li>Kontakt</li></ul></div>
    <div><h6>RECHTLICHES</h6><ul><li>AGB</li><li>Datenschutz</li><li>Cookies</li><li>Impressum</li></ul><h6 style="margin:10px 0 0">PARTNER</h6><div class="badge"></div></div>
    <span class="fmark">SELVADON</span>
  </footer>
</section>

</div>
</body>
</html>
```